Business Card Design for Marketing Firm

Looking for business card design for higher end marketing firm. Clean but impressionable/trendy. We are a marketing firm that represents manufacturers in the foodservice equipment and supply industry. Our customers are end users such has hotels, restaurants, country clubs, convention centers and casinos as well as distributors of restaurants supplies and equipment, and manufacturers of foodservice equipment and supplies.
Target Market(s)
Hotels, Restaurants, Supply & Equipment Distributors, Foodservice Manufacturers
Industry/Entity Type
Foodservice/Hospitality
Contact Information for Business Card
Name, Title, Contact Number, Email, Website, Social Media, Address
Requirements
Must have
- Clean & Simple but Serious and Impressionable

```html
<!DOCTYPE html>
<html lang="en">
<head>
<meta charset="utf-8">
<title>Meridian Hospitality Reps – Business Card</title>
<link href="https://fonts.googleapis.com/css2?family=Cinzel:wght@600;700&family=Arimo:wght@400&display=swap" rel="stylesheet">
<style>
  :root {
    --page-bg: #efeeec;
    --card-top: #ecebe9;
    --card-bottom: #dcd9d5;
    --card-edge: #b9b6b2;
    --navy: #1f2152;
    --ink: #1c1c24;
    --muted: #55555e;
    --rule: #2a2a33;
  }
  * { box-sizing: border-box; margin: 0; padding: 0; }
  html, body {
    width: 1170px;
    height: 1200px;
    overflow: hidden;
    background: var(--page-bg);
  }
  .canvas {
    position: relative;
    width: 1170px;
    height: 1200px;
  }
  .card {
    position: absolute;
    left: 60px;
    top: 301px;
    width: 1050px;
    height: 598px;
    border-radius: 30px;
    border: 1.5px solid var(--card-edge);
    background: linear-gradient(160deg, var(--card-top), var(--card-bottom));
    box-shadow: 0 10px 30px rgba(0,0,0,0.08);
  }
  .social {
    position: absolute;
    left: 70px;
    top: 48px;
    display: flex;
    gap: 8px;
  }
  .social-dot {
    width: 37px;
    height: 37px;
    border-radius: 50%;
    background: var(--navy);
  }
  .brand {
    position: absolute;
    right: 67px;
    top: 190px;
    text-align: right;
    font-family: "Cinzel", serif;
    font-weight: 600;
    color: var(--navy);
  }
  .brand-name {
    font-size: 34px;
    letter-spacing: 0.5px;
    line-height: 1;
  }
  .brand-rule {
    position: absolute;
    left: 0;
    top: 45px;
    width: 312px;
    height: 3px;
    background: var(--navy);
  }
  .brand-sub {
    margin-top: 6px;
    font-size: 24px;
    line-height: 1;
  }
  .person {
    position: absolute;
    left: 68px;
    top: 362px;
    font-family: "Cinzel", serif;
  }
  .person-name {
    font-weight: 700;
    font-size: 41px;
    color: var(--navy);
    line-height: 1;
    letter-spacing: 0.5px;
  }
  .person-title {
    margin-top: 6px;
    font-family: "Arimo", sans-serif;
    font-size: 24px;
    color: var(--muted);
  }
  .divider {
    position: absolute;
    left: 68px;
    right: 70px;
    top: 452px;
    height: 1.5px;
    background: var(--rule);
  }
  .contact {
    position: absolute;
    left: 68px;
    top: 467px;
    font-family: "Arimo", sans-serif;
    font-size: 25px;
    color: var(--muted);
    line-height: 33px;
  }
  .contact-line {
    display: flex;
    align-items: center;
    gap: 10px;
  }
  .contact-icon {
    width: 22px;
    height: 22px;
    fill: var(--navy);
  }
  .address {
    position: absolute;
    right: 70px;
    top: 465px;
    text-align: right;
    font-family: "Arimo", sans-serif;
    font-size: 25px;
    color: var(--ink);
    line-height: 33px;
  }
</style>
</head>
<body>
<main class="canvas">
  <section class="card" aria-label="Business card">
    <div class="social" aria-label="Social media">
      <span class="social-dot"></span>
      <span class="social-dot"></span>
      <span class="social-dot"></span>
    </div>

    <div class="brand">
      <div class="brand-name">Meridian Hospitality</div>
      <span class="brand-rule"></span>
      <div class="brand-sub">Reps</div>
    </div>

    <div class="person">
      <div class="person-name">Owen Carter</div>
      <div class="person-title">President</div>
    </div>

    <div class="divider"></div>

    <div class="contact">
      <div class="contact-line">
        <svg class="contact-icon" viewBox="0 0 24 24" aria-hidden="true"><path d="M6.6 10.8a15.1 15.1 0 0 0 6.6 6.6l2.2-2.2a1 1 0 0 1 1-.25 11.4 11.4 0 0 0 3.6.57 1 1 0 0 1 1 1V20a1 1 0 0 1-1 1A17 17 0 0 1 3 4a1 1 0 0 1 1-1h3.5a1 1 0 0 1 1 1c0 1.25.2 2.45.57 3.57a1 1 0 0 1-.25 1z"/></svg>
        <span>(555) 0142-7781</span>
      </div>
      <div class="contact-line">
        <svg class="contact-icon" viewBox="0 0 24 24" aria-hidden="true"><path d="M3 6h18v12H3z M3 6l9 7 9-7" fill="var(--navy)"/><path d="M3 6l9 7 9-7" fill="none" stroke="#dcd9d5" stroke-width="1.6"/></svg>
        <span>name@MERIDIAN.com</span>
      </div>
    </div>

    <div class="address">
      <div>2170 Lindenwood Avenue</div>
      <div>Glen Haven, NY 11020</div>
    </div>
  </section>
</main>
</body>
</html>
```